TeeWiseHub Stationery and Style Guide, You set the tone! (logo Provided)

TeewiseHub is a new and exciting business that will be focusing on providing quality golf information for all Australian golfers.

We already have a great logo and now we are looking to style our documents.

We would like to see the following:

- Front cover page Design including(logo, branding statement and Document title) Branding statement is Every Green - Every Player
- Sales Document design, this is our main document and we would like you to spend most time on this document. I have attached a sample PDF with the basic layout. but you will need to add some flair to the document and make it look great.
- A Dot point design explaining points in an image (I have attached a sample to show what I mean) Please include this image in the Sales Document
- A footnote for all documents(containing, small logo, branding statement and website address)
- An email signature (containing: logo, Dov Hallberg, dov@teewisehub.com.au, 0471 529 318, www.teewisehub.com.au)

The font used in the logo is borisblackboxx.
At this stage we don't need business cards or envelopes please.

A little background:
The service will be providing:

• A Website that allows all Australian golfers to find golf courses close to them on a simple to use Google map
• Browse golf courses on a map or by search.
• View full information about a golf course including images, facilities, prices and full contact details.
• Mobile version of the website for Iphone, Android and other mobile platforms.
• We will use the users GPS location to show them where they are and what golf courses are near them.
• All golf courses will be able to show specials and other deals for all visitors.

Thank you for looking at our project and we look forward to your designs.

Target Market(s)

All Australian Golfers

Industry/Entity Type

Golf Course

Requirements
Must have
• A great Sales Document Design as that is the main stationery document we will be using.
Please use the sample Sales Document for sample content and basic elements needed.
Should not have
• We don't need business cards and envelope design.

```html
<!DOCTYPE html>
<html lang="en">
<head>
<meta charset="utf-8">
<title>TeewiseHub Email Signature</title>
<link rel="stylesheet" href="https://fonts.googleapis.com/css2?family=Lato:wght@300;700&family=Arimo:wght@700&display=swap">
<style>
  :root {
    --page: #ffffff;
    --green-soft: #8cc63f;
    --green-name: #7ab648;
    --green-light: #8dc63f;
    --green-deep: #6ab23e;
    --mascot-tone-a: #a98b6a;
    --mascot-tone-b: #6e5338;
    --white: #ffffff;
  }
  * { margin: 0; padding: 0; box-sizing: border-box; }
  html, body {
    width: 1200px;
    height: 900px;
    overflow: hidden;
    background: var(--page);
  }
  .signature {
    position: absolute;
    left: 110px;
    top: 250px;
    width: 980px;
  }
  .signature__closing {
    font-family: "Lato", sans-serif;
    font-weight: 300;
    font-size: 34px;
    color: var(--green-soft);
    line-height: 1.4;
  }
  .signature__name {
    font-family: "Lato", sans-serif;
    font-weight: 700;
    font-size: 34px;
    color: var(--green-name);
    line-height: 1.4;
    margin-bottom: 36px;
  }
  .signature__banner {
    display: block;
    width: 980px;
    height: 231px;
  }
  .banner__brand,
  .banner__tagline,
  .banner__contact {
    font-family: "Arimo", sans-serif;
    font-weight: 700;
    fill: var(--white);
  }
</style>
</head>
<body>
  <section class="signature">
    <p class="signature__closing">Sincerely,</p>
    <p class="signature__name">Dov Hallberg</p>

    <svg class="signature__banner" viewBox="0 0 573 135" xmlns="http://www.w3.org/2000/svg">
      <defs>
        <linearGradient id="mascotTone" x1="0" y1="0" x2="0" y2="1">
          <stop offset="0" stop-color="var(--mascot-tone-a)"/>
          <stop offset="1" stop-color="var(--mascot-tone-b)"/>
        </linearGradient>
      </defs>

      <path class="banner__wave-light" fill="var(--green-light)"
            d="M0,40 C120,80 220,75 320,55 C420,35 500,30 573,60 L573,80 C480,40 400,50 300,70 C200,90 120,95 0,60 Z"/>
      <path class="banner__wave-deep" fill="var(--green-deep)"
            d="M0,60 C120,95 200,90 300,70 C400,50 480,40 573,80 L573,135 L0,135 Z"/>

      <rect class="banner__mascot" role="img" aria-label="Golf mascot character holding a club"
            x="40" y="8" width="70" height="62" rx="12" fill="url(#mascotTone)"/>

      <text class="banner__brand" x="28" y="97" font-size="30">TeewiseHub</text>
      <text class="banner__tagline" x="42" y="116" font-size="11">Every Green, Every Player</text>

      <text class="banner__contact" x="424" y="82" font-size="11">0471 529 318,</text>
      <text class="banner__contact" x="424" y="99" font-size="11">dov@teewisehub.com.au,</text>
      <text class="banner__contact" x="424" y="116" font-size="11">www.teewisehub.com.au</text>
    </svg>
  </section>
</body>
</html>
```